Business Card Design

New business card design

Target Market(s)

Residential & Commercial Property Managers

Industry/Entity Type

Plumbing Services

Contact Information for Business Card

Name - Owen Tredgold, title - Director, Phone Number - 0431 862 507, email - owen@rvb-plumbing.com.au, Company ABN - 73 215 904 386,

Font styles to use
Sans Serif

Colors
0054AA
0677BA
7BADD7
CADEEF
E8F1F8

```html
<!DOCTYPE html>
<html lang="en">
<head>
<meta charset="utf-8">
<title>RVB Plumbing Services – Business Card</title>
<link href="https://fonts.googleapis.com/css2?family=Poppins:wght@300;400;500;600&display=swap" rel="stylesheet">
<style>
  :root {
    --backdrop: #222222;
    --card-front: #ebe9e7;
    --card-back: #29a8e0;
    --brand-blue: #2a9bd8;
    --ink: #1a1f26;
    --surname: #6b6259;
    --logo-ink: #1d2733;
    --logo-light: #e8f1f8;
  }
  * { box-sizing: border-box; margin: 0; padding: 0; }
  html, body {
    width: 1200px; height: 780px; overflow: hidden;
    background: var(--backdrop);
    font-family: "Poppins", sans-serif;
  }
  .stage {
    position: relative; width: 1200px; height: 780px;
    display: flex; align-items: center; justify-content: center; gap: 60px;
  }
  .card {
    position: relative; width: 520px; height: 300px;
    border-radius: 18px; overflow: hidden;
  }
  .card--front { background: var(--card-front); color: var(--ink); }
  .card--back { background: var(--card-back); display: flex; align-items: center; justify-content: center; }

  .divider { position: absolute; inset: 0; width: 520px; height: 300px; }

  .brand {
    position: absolute; left: 40px; top: 62px; width: 200px;
    font-weight: 300; color: var(--logo-ink); text-align: center; line-height: 1;
  }
  .brand__name { font-size: 64px; letter-spacing: 2px; }
  .brand__tag { font-size: 9px; letter-spacing: 5px; margin-top: 8px; }

  .abn {
    position: absolute; left: 40px; bottom: 42px; width: 200px; text-align: center;
    font-size: 12px; color: var(--brand-blue); letter-spacing: .3px;
  }

  .person { position: absolute; left: 290px; top: 92px; }
  .person__name { font-size: 26px; line-height: 1; white-space: nowrap; }
  .person__first { color: var(--brand-blue); font-weight: 600; }
  .person__last { color: var(--surname); font-weight: 300; }
  .person__title { font-size: 12px; font-weight: 500; margin-top: 4px; }

  .contacts { position: absolute; left: 272px; top: 160px; list-style: none; }
  .contacts li {
    display: flex; align-items: center; gap: 8px;
    font-size: 13px; line-height: 22px; white-space: nowrap;
  }
  .contacts svg { width: 12px; height: 12px; flex: none; }

  .brand--back { position: static; width: auto; color: var(--logo-light); }
  .brand--back .brand__name { font-size: 96px; }
  .brand--back .brand__tag { font-size: 11px; letter-spacing: 8px; margin-top: 12px; }
</style>
</head>
<body>
<main class="stage">
  <section class="card card--front" aria-label="Business card front">
    <svg class="divider" viewBox="0 0 520 300" aria-hidden="true">
      <line x1="300" y1="40" x2="225" y2="250" stroke="var(--brand-blue)" stroke-width="1"/>
    </svg>
    <div class="brand">
      <div class="brand__name">rvb</div>
      <div class="brand__tag">plumbing services</div>
    </div>
    <p class="abn">ABN - 73 215 904 386,</p>

    <div class="person">
      <p class="person__name"><span class="person__first">Owen</span> <span class="person__last">Tredgold</span></p>
      <p class="person__title">Director</p>
    </div>

    <ul class="contacts">
      <li>
        <svg viewBox="0 0 12 12" aria-hidden="true"><path d="M3 1.5l1.6 2.3-1 1a6 6 0 0 0 3.6 3.6l1-1L10.5 9l-.9 1.5C5.5 10.5 1.5 6.5 1.5 2.4z" fill="var(--brand-blue)"/></svg>
        0431 862 507
      </li>
      <li>
        <svg viewBox="0 0 12 12" aria-hidden="true"><rect x="1" y="2.5" width="10" height="7" rx="1" fill="var(--brand-blue)"/><path d="M1.5 3.2L6 6.6l4.5-3.4" fill="none" stroke="#fff" stroke-width="1"/></svg>
        owen@rvb-plumbing.com.au
      </li>
      <li>
        <svg viewBox="0 0 12 12" aria-hidden="true"><circle cx="6" cy="6" r="5" fill="var(--brand-blue)"/><path d="M1 6h10M6 1c2 2.5 2 7.5 0 10M6 1c-2 2.5-2 7.5 0 10" fill="none" stroke="#fff" stroke-width=".7"/></svg>
        www.rvb-plumbing.com.au
      </li>
    </ul>
  </section>

  <section class="card card--back" aria-label="Business card back">
    <div class="brand brand--back">
      <div class="brand__name">rvb</div>
      <div class="brand__tag">plumbing services</div>
    </div>
  </section>
</main>
</body>
</html>
```